Workvine banner ad for roofing company

We need an ad created for a Workvine banner advertising campaign for a UK based roofing company.

The design should have a large photograph on the background (see attached).
The design should have our Ratewell rating (5 stars).
There should be a large text header at the top which reads "Your local roofing experts"

The following services should be listed:
- New roofs
- General roof repairs
- Drone surveys
- Single ply roofing
- Steel cladding
- Asbestos removal

The company logo needs to be visible (attached). Also the company telephone number 020 7946 0321 and website www.brantleyroofing.com

The advert needs to be horizontal/landscape design. For full spec, please see here: https://business.workvine-example.com/marketing-solutions/success/ads-guide/single-image-ads

Size required: 1.91:1 - 1200 x 628 pixels

```html
<!DOCTYPE html>
<html lang="en">
<head>
<meta charset="utf-8">
<title>Brantley Roofing – Your local roofing experts</title>
<link rel="stylesheet" href="https://fonts.googleapis.com/css2?family=Outfit:wght@500;600;700&display=swap">
<style>
  :root {
    --navy: #0f4a7c;
    --sky-blue: #1a95c9;
    --bright-blue: #18a3dc;
    --slate: #3c4a53;
    --rating-green: #1fb77a;
    --ink: #1e2a30;
    --sky-top: #dfe3e6;
    --sky-mid: #c7ced3;
    --roof-dark: #4b5560;
  }
  * { margin: 0; padding: 0; box-sizing: border-box; }
  html, body { width: 1200px; height: 628px; overflow: hidden; background: #fff; }
  .banner {
    position: relative;
    width: 1200px;
    height: 628px;
    overflow: hidden;
    font-family: "Outfit", "Century Gothic", sans-serif;
  }
  .hero-photo {
    position: absolute;
    inset: 0;
    background:
      linear-gradient(168deg, transparent 0 46%, #5a6470 47%, var(--roof-dark) 100%),
      linear-gradient(180deg, var(--sky-top) 0%, var(--sky-mid) 60%, #aeb8bf 100%);
  }
  .overlay { position: absolute; inset: 0; }
  .headline {
    position: absolute;
    left: 72px;
    top: 30px;
    font-weight: 700;
    font-size: 60px;
    line-height: 54px;
    letter-spacing: -0.5px;
  }
  .headline .line-one { display: block; color: var(--navy); }
  .headline .line-two { display: block; color: var(--sky-blue); padding-left: 10px; }
  .services {
    position: absolute;
    left: 82px;
    top: 184px;
    list-style: none;
    color: var(--slate);
    font-weight: 600;
    font-size: 37px;
    line-height: 50.5px;
  }
  .brand {
    position: absolute;
    right: 31px;
    top: 30px;
    display: flex;
    align-items: center;
    gap: 10px;
  }
  .brand-dot {
    width: 46px; height: 46px;
    border-radius: 50%;
    background: var(--navy);
  }
  .brand-name {
    font-weight: 700;
    font-size: 44px;
    line-height: 1;
    color: var(--bright-blue);
    letter-spacing: -1px;
  }
  .contact {
    position: absolute;
    right: 31px;
    top: 82px;
    text-align: right;
    font-weight: 600;
    font-size: 19px;
    line-height: 23px;
  }
  .contact .phone { color: var(--bright-blue); }
  .contact .web { color: var(--navy); letter-spacing: 0.3px; }
  .rating {
    position: absolute;
    left: 96px;
    top: 535px;
  }
  .rating-name {
    display: flex;
    align-items: center;
    gap: 8px;
    font-weight: 500;
    font-size: 28px;
    line-height: 1;
    color: var(--ink);
  }
  .rating-mark {
    width: 24px; height: 24px;
    background: var(--rating-green);
  }
  .rating-bar {
    margin-top: 8px;
    width: 154px;
    height: 29px;
    background: var(--rating-green);
  }
</style>
</head>
<body>
  <div class="banner">
    <div class="hero-photo" role="img" aria-label="Photograph of a roofer in a yellow hard hat kneeling on a grey shingle roof with a hammer and toolbox, under an overcast sky"></div>

    <svg class="overlay" width="1200" height="628" viewBox="0 0 1200 628" aria-hidden="true">
      <defs>
        <linearGradient id="blue-wash" x1="0" y1="0" x2="1" y2="0.4">
          <stop offset="0" stop-color="#bfe3f1" stop-opacity="0.55"/>
          <stop offset="0.6" stop-color="#5fc0e0" stop-opacity="0.55"/>
          <stop offset="1" stop-color="#2aa8d8" stop-opacity="0.6"/>
        </linearGradient>
      </defs>
      <polygon points="0,0 490,0 673,305 470,628 0,628" fill="url(#blue-wash)"/>
      <rect x="60" y="168" width="410" height="345" fill="#ffffff" opacity="0.18"/>
    </svg>

    <h1 class="headline">
      <span class="line-one">Your local</span>
      <span class="line-two">roofing experts</span>
    </h1>

    <ul class="services">
      <li>New roofs</li>
      <li>General roof repairs</li>
      <li>Drone surveys</li>
      <li>Single ply roofing</li>
      <li>Steel cladding</li>
      <li>Asbestos removal</li>
    </ul>

    <div class="brand">
      <span class="brand-dot"></span>
      <span class="brand-name">brantleyroofing</span>
    </div>
    <div class="contact">
      <div class="phone">020 7946 0321</div>
      <div class="web">www.brantleyroofing.com</div>
    </div>

    <div class="rating" aria-label="Ratewell rating: 5 stars">
      <div class="rating-name"><span class="rating-mark"></span>Ratewell</div>
      <div class="rating-bar"></div>
    </div>
  </div>
</body>
</html>
```